Broadway Haulage website

We need a website design for a towing company based in Australia.
The design should be simple and minimalist. The site can be in colours of the logo are Blue, Red and White (see attached) - but we'd like to see options in some sort of industrial looking metallic theme if possible.
We base our business on our friendly and efficient customer service, the design should attempt to convey this in some way.

Industry/Entity Type

Industrial

Font styles to use
Sans Serif

```html
<!DOCTYPE html>
<html lang="en">
<head>
<meta charset="utf-8">
<title>Broadway Haulage</title>
<link href="https://fonts.googleapis.com/css2?family=Open+Sans:ital,wght@0,400;0,600;0,700;1,400;1,600;1,700&display=swap" rel="stylesheet">
<style>
:root{
  --red:#cc0a0f;
  --red-dark:#a5080d;
  --blue:#0b3d8c;
  --blue-deep:#0a3a8a;
  --text:#555;
  --band-light:#c9b21a;
  --band-dark:#5e5520;
  --white:#fff;
  --line:#d8d8d8;
}
*{box-sizing:border-box;margin:0;padding:0}
html,body{width:758px;height:1200px;overflow:hidden}
body{position:relative;font-family:"Open Sans",sans-serif;background:var(--white);color:var(--text)}
.abs{position:absolute}
.edge-band{position:absolute;left:0;width:758px;height:6px;
  background:linear-gradient(90deg,var(--band-dark),var(--band-light) 50%,var(--band-dark))}
.header-band{position:absolute;left:0;top:0;width:758px;height:330px;
  background:linear-gradient(90deg,#bdbdbd,#e6e6e6 30%,#f2f2f2 50%,#dcdcdc 70%,#b9b9b9)}
.brand{left:86px;top:14px;display:flex;align-items:center;gap:10px}
.brand-mark{width:60px;height:60px;border-radius:50%;background:var(--blue)}
.brand-name{font-size:21px;font-weight:700;color:var(--blue);line-height:1.05;width:150px}
.phone{left:515px;top:30px;display:flex;gap:8px}
.phone-label{font-size:12px;font-style:italic;font-weight:600;color:var(--white);text-shadow:0 1px 1px #777}
.phone-number{font-size:19px;font-style:italic;font-weight:700;color:#222;line-height:1.2}
.nav{left:82px;top:93px;width:593px;height:32px;background:var(--red);display:flex;align-items:center;justify-content:space-between;padding:0 12px}
.nav a{color:var(--white);font-size:8px;font-weight:700;font-style:italic;text-decoration:none;letter-spacing:.3px}
.slider{left:82px;top:125px;width:593px;height:244px;background:#d5d5d5;padding:4px}
.slider-photo{width:100%;height:100%;background:linear-gradient(180deg,#7fb3e6 0%,#b9d6ef 35%,#9c8f8f 60%,#6e6e6e 85%,#555 100%)}
.slider-caption{left:371px;top:202px;width:300px;height:90px;background:rgba(255,255,255,.82);text-align:right;padding:8px 12px 0 20px}
.slider-caption h1{font-size:20px;font-weight:600;color:var(--blue);line-height:1.12}
.btn-red{display:inline-block;background:var(--red);color:var(--white);font-size:10px;font-weight:600;padding:4px 7px;margin-top:5px;border:1px solid #fff}
.dots{left:349px;top:341px;display:flex;gap:4px}
.dots span{width:12px;height:12px;border-radius:50%;background:#dedede}
.dots span:first-child{background:var(--white)}
.section-title{font-size:15px;font-weight:700;font-style:italic;color:var(--blue);letter-spacing:.2px}
.welcome-title{left:84px;top:387px}
.welcome-photo{left:82px;top:417px;width:138px;height:113px;background:linear-gradient(180deg,#9cc0e2,#d8d8d8 55%,#9a9a9a)}
.welcome-text{left:234px;top:414px;width:440px;font-size:8px;line-height:14px;color:var(--text)}
.welcome-text p+p{margin-top:3px}
.divider{left:82px;top:548px;width:593px;height:1px;background:var(--line)}
.services{left:82px;top:564px;width:442px;height:242px;background:linear-gradient(90deg,#c4c4c4,#e2e2e2 50%,#c8c8c8)}
.services .section-title{position:absolute;left:14px;top:13px}
.services .edge-band{top:236px;width:442px}
.service{position:absolute;width:126px}
.service-photo{height:62px;background:linear-gradient(180deg,#6fa5db,#c8d6e0 45%,#8a8a8a)}
.service-name{height:19px;background:#1a1a1a;color:var(--white);font-size:8.5px;padding-left:8px;line-height:19px}
.contact{left:537px;top:564px;width:138px;height:242px;background:var(--blue-deep)}
.contact-head{height:24px;background:var(--red);color:var(--white);font-size:12px;font-weight:700;font-style:italic;padding:4px 9px}
.contact label{display:block;font-size:7.5px;font-weight:600;color:var(--white);margin:7px 0 3px 10px}
.contact .field{margin-left:10px;width:118px;height:17px;background:var(--white);border-radius:2px}
.contact .field.tall{height:53px}
.contact .submit{position:absolute;left:60px;top:210px;width:68px;height:20px;background:var(--red);color:var(--white);font-size:7.5px;font-weight:600;text-align:center;line-height:20px;border-radius:2px}
.card{position:absolute;top:822px;width:189px;height:202px;background:#f5f5f5;border:1px solid var(--line);padding:10px 12px}
.card .section-title{font-size:14px}
.card-photo{margin-top:7px;height:84px;background:linear-gradient(180deg,#a9c6dd,#8b7d78 50%,#5c5c5c)}
.card p{font-size:8px;line-height:14px;margin-top:8px}
.more{position:absolute;left:12px;bottom:14px;font-size:8px;font-weight:600;color:var(--red)}
.quote{font-size:7.5px;font-style:italic;line-height:12.5px;margin-top:6px;padding-top:2px}
.quote b{font-size:16px;color:#aaa;font-style:normal;font-weight:700;vertical-align:-4px;margin-right:3px;line-height:0}
.quote .by{display:block;text-align:right;color:var(--red);margin-top:4px}
.quote+.quote{border-top:1px solid var(--line);margin-top:7px;padding-top:7px}
.video-photo{position:relative}
.play{position:absolute;left:70px;top:28px;width:26px;height:26px}
.footer{left:0;top:1039px;width:758px;height:155px;background:linear-gradient(180deg,#c20d12,#a50a0e)}
.footer h3{font-size:11.5px;font-weight:600;font-style:italic;color:var(--white)}
.footer .col{position:absolute;top:16px;color:var(--white);font-size:8px}
.footer ul{list-style:none;margin-top:5px}
.footer li{line-height:14.5px}
.news-date{font-weight:700;margin-top:9px}
.news-body{line-height:13px;width:175px}
.read{font-weight:600;margin-top:12px}
.arrows{position:absolute;left:148px;top:2px;font-size:10px;opacity:.8}
.social li{display:flex;align-items:center;gap:8px;line-height:20.5px}
.social i{width:13px;height:13px;background:var(--white);opacity:.9;border-radius:2px}
.footer-brand{left:540px;top:18px;width:130px;text-align:center}
.footer-brand .brand-mark{width:56px;height:56px;margin:0 auto 6px;background:var(--white)}
.footer-brand .name{font-size:9px;font-weight:700;color:var(--white)}
.footer-brand .legal{font-size:7.5px;font-style:italic;line-height:13px;margin-top:14px;color:#f3dada}
</style>
</head>
<body>
<div class="edge-band" style="top:0" role="img" aria-label="Safety stripe band"></div>
<div class="header-band"></div>

<div class="abs brand">
  <span class="brand-mark"></span>
  <span class="brand-name">Broadway Haulage</span>
</div>

<div class="abs phone">
  <svg width="20" height="22" viewBox="0 0 20 22"><path d="M4 2c2-1 3 0 4 3l-2 2c1 3 3 6 6 8l2-2c3 1 4 2 3 4l-2 2C9 20 2 12 2 4z" fill="var(--red)"/></svg>
  <div><div class="phone-label">Call Us Today:</div><div class="phone-number">1800 555 0199</div></div>
</div>

<nav class="abs nav">
  <a>HOME</a><a>ABOUT US</a><a>TOWING SERVICES</a><a>QUOTE REQUEST</a><a>GALLERY</a><a>TESTIMONIALS</a><a>CONTACT US</a>
</nav>

<div class="abs slider"><div class="slider-photo" role="img" aria-label="Red prime mover hauling a motorhome on a low loader trailer"></div></div>
<div class="abs slider-caption">
  <h1>We Provide Towing Services in Australia</h1>
  <span class="btn-red">Request a Quote</span>
</div>
<div class="abs dots"><span></span><span></span><span></span><span></span></div>

<h2 class="abs section-title welcome-title">WELCOME TO OUR COMPANY</h2>
<div class="abs welcome-photo" role="img" aria-label="Tilt tray tow truck loading a white four wheel drive"></div>
<div class="abs welcome-text">
  <p>Lorem ipsum dolor sit amet, consect- etuer adipiscing elit, sed diam nonummy nibh euismod tincidunt ut laoreet dolore magna aliquam erat volutpat. Ut wisi enim ad minim veniam, quis nostrud exerci tation ullam. Consectetuer adipiscing elit, sed diam nonummy nibh euismod tincidunt ut laoreet dolore magna aliquam erat volut- pat. Ut wisi enim ad minim veniam, quis nostrud exerci tation ullam.</p>
  <p>Nunc consequat congue nulla eu imperdiet. Donec in est erat, id malesuada turpis. Nunc a dui id turpis</p>
  <p>convallis semper. Nunc dignissim lectus vitae eros placerat euismod. Aenean lacinia sodales eros, sit amet molestie enim consectetur eget. Sed vel magna vel eros adipiscing adipiscing eu sit amet turpis. Mauris et massa sed lacus tempus pellentesque.</p>
</div>
<div class="abs divider"></div>

<section class="abs services">
  <h2 class="section-title">TOWING SERVICES</h2>
  <div class="service" style="left:14px;top:42px"><div class="service-photo" role="img" aria-label="Tow truck carrying a car"></div><div class="service-name">Service Heading</div></div>
  <div class="service" style="left:159px;top:42px"><div class="service-photo" role="img" aria-label="Bus on a tow truck"></div><div class="service-name">Service Heading</div></div>
  <div class="service" style="left:303px;top:42px"><div class="service-photo" role="img" aria-label="Truck loaded onto a carrier"></div><div class="service-name">Service Heading</div></div>
  <div class="service" style="left:14px;top:145px"><div class="service-photo" role="img" aria-label="Heavy haulage road train"></div><div class="service-name">Service Heading</div></div>
  <div class="service" style="left:159px;top:145px"><div class="service-photo" role="img" aria-label="Machinery on a heavy trailer"></div><div class="service-name">Service Heading</div></div>
  <div class="service" style="left:303px;top:145px"><div class="service-photo" role="img" aria-label="Loader and vehicles on a low loader"></div><div class="service-name">Service Heading</div></div>
  <div class="edge-band" role="img" aria-label="Safety stripe band"></div>
</section>

<aside class="abs contact">
  <div class="contact-head">QUICK CONTACT</div>
  <label>Name:</label><div class="field"></div>
  <label>Contact No:</label><div class="field"></div>
  <label>Email Address:</label><div class="field"></div>
  <label>Enter Message:</label><div class="field tall"></div>
  <div class="submit">SUBMIT NOW</div>
</aside>

<section class="card" style="left:82px">
  <h2 class="section-title">GALLERY</h2>
  <div class="card-photo" role="img" aria-label="Red truck hauling machinery on a trailer"></div>
  <p>Nunc dignissim lectus vitae eros placerat euismod. Aenean lacinia sodales eros, sit amet molestie enim consectetur eget.</p>
  <span class="more">VIEW ALL &gt;&gt;</span>
</section>

<section class="card" style="left:284px">
  <h2 class="section-title">TESTIMONIALS</h2>
  <div class="quote"><b>&ldquo;</b>Nunc dignissim lectus vitae eros placerat euismod. Aenean lacinia sodales eros, sit amet molestie adipiscing ..<span class="by">- Daniel Roe</span></div>
  <div class="quote"><b>&ldquo;</b>Nunc dignissim lectus vitae eros placerat euismod. Aenean lacinia sodales eros, sit amet molestie adipiscing ..<span class="by">- Daniel Roe</span></div>
  <span class="more">READ ALL TESTIMONIALS &gt;&gt;</span>
</section>

<section class="card" style="left:486px">
  <h2 class="section-title">WATCH A VIDEO</h2>
  <div class="card-photo video-photo" role="img" aria-label="Video still of a tow truck in a yard" style="height:101px;background:linear-gradient(180deg,#bfc9cf,#9a9680 55%,#6d6d66)">
    <svg class="play" viewBox="0 0 26 26"><circle cx="13" cy="13" r="11.5" fill="rgba(0,0,0,.35)" stroke="#fff" stroke-width="2"/><path d="M10 7l9 6-9 6z" fill="#fff"/></svg>
  </div>
  <p>Nunc dignissim lectus vitae eros placerat euismod.</p>
  <span class="more">VIEW ALL VIDEOS &gt;&gt;</span>
</section>

<footer class="abs footer">
  <div class="col" style="left:82px">
    <h3>LATEST NEWS</h3><span class="arrows">&lsaquo;&nbsp;&nbsp;&rsaquo;</span>
    <div class="news-date">Feb 20, 2014</div>
    <div class="news-body">Nunc dignissim lectus vitae eros placerat euismod. Aenean lacinia sodales eros, sit amet molestie adipiscing ..</div>
    <div class="read">Read More &gt;&gt;</div>
  </div>
  <div class="col" style="left:294px">
    <h3>QUICK LINKS</h3>
    <ul><li>Home</li><li>About Us</li><li>Towing Services</li><li>Request Quote</li><li>Gallery</li><li>Testimonials</li><li>Contact Us</li></ul>
  </div>
  <div class="col" style="left:422px">
    <h3>CONNECT US</h3>
    <ul class="social"><li><i></i>Social Page</li><li><i></i>Microblog</li><li><i></i>Rss Feeds</li><li><i></i>Video Channel</li></ul>
  </div>
  <div class="abs footer-brand">
    <div class="brand-mark"></div>
    <div class="name">Broadway Haulage</div>
    <div class="legal">Copyright &copy; 2014. All Right Reserved<br>Terms of Services</div>
  </div>
</footer>
<div class="edge-band" style="top:1194px" role="img" aria-label="Safety stripe band"></div>
</body>
</html>
```